Maelis Spacial\floral Decorator

Maelis is a spacial\floral decorator. She is passionate about Art, Life, Architecture, Painting, Music and movement. Her website will be used to showcase her spacial and floral design projects.
We are looking for a very unique website that stands apart from the crowd.
We believe that is achieved through simple high quality design Simple being very important.
The Home page should display primarily photos.
Your task is to provide an un-coded homepage template.
The page must be dynamic in its style and feel.

Maelis has suggest a grid pattern for the images, similar to this http://www.dorvanbloomhouse.co.uk. Overall We like the look and feel of this site.

We like the following color palettes, please base your design around one of them;
https://tintrova.example.com/#themes/search?term=5531704
https://tintrova.example.com/#themes/search?term=5536218
https://tintrova.example.com/#themes/search?term=5548126
https://tintrova.example.com/#themes/search?term=5540967
https://tintrova.example.com/#themes/search?term=5537419

Our target Market is High End Corporate Clients, located in Shanghai and Taipai. For these clients she utilise her floral and interior design skills to decorate a space. See Photos 2, 3 and 21 for examples.
She also targets High End personal clients for events such as weddings and gift combination i.e. flowers and something else.

Requirements
Must have
• Chinese/ English Language Selection
A selection of pictures that appear and disappear.
A menu system that includes:
Home – Portfolio – About Maelis – Blog – Contact Her
A very subtle menu system linking to chatnest, worklinq On, v+ and xunmo.
Nice to have
• We also like the use of an image for the background but this is not necessary.
Should not have
• Alot of Text, yes we now this isn't great for SEO but we will deal with that on other pages

```html
<!DOCTYPE html>
<html lang="en">
<head>
<meta charset="utf-8">
<title>Maelis — Spacial &amp; Floral Decorator</title>
<link rel="stylesheet" href="https://fonts.googleapis.com/css2?family=Didact+Gothic&family=Questrial&family=Montserrat:wght@700&display=swap">
<style>
  :root {
    --page: #f9f9f9;
    --ink: #2b2b2b;
    --ink-soft: #8a8a8a;
    --rule: #e6e4ea;
    --frame: #dcd6e2;
    --white: #ffffff;
    --label-bg: #1f0b16;
  }
  * { margin: 0; padding: 0; box-sizing: border-box; }
  html, body { width: 1042px; height: 1200px; overflow: hidden; background: var(--page); }
  body { position: relative; font-family: "Questrial", sans-serif; color: var(--ink); }

  .site-nav { position: absolute; top: 88px; left: 260px; width: 520px; height: 34px; font-family: "Didact Gothic", sans-serif; }
  .site-nav a { position: absolute; bottom: 2px; color: var(--ink); text-decoration: none; white-space: nowrap; }
  .nav-home { left: 0; font-size: 30px; line-height: 1; color: #555; }
  .nav-about { left: 135px; font-size: 18px; }
  .nav-contact { left: 279px; font-size: 18px; color: #888; }
  .lang-switch { position: absolute; right: 0; bottom: 4px; font-size: 13px; color: #888; }
  .lang-switch .divider { color: var(--ink); margin: 0 6px; }

  .about-panel { position: absolute; top: 122px; left: 260px; width: 519px; height: 519px; overflow: hidden; }
  .about-photo { position: absolute; inset: 0;
    background:
      radial-gradient(ellipse 160px 200px at 200px 360px, rgba(226,150,110,.85), transparent 70%),
      linear-gradient(100deg, #c47a3c 0%, #a1506c 30%, #5c2a8e 60%, #2d1c7c 100%); }
  .active-marker { position: absolute; top: 0; left: 170px; width: 0; height: 0;
    border-left: 12px solid transparent; border-right: 12px solid transparent; border-top: 12px solid var(--page); }
  .about-copy { position: absolute; color: var(--white); font-size: 9.6px; line-height: 15.2px; hyphens: auto; -webkit-hyphens: auto; }
  .about-intro { top: 34px; left: 32px; width: 456px; text-align: justify; }
  .drop-cap { float: left; font-size: 32px; line-height: 28px; margin: 2px 4px 0 0; }
  .about-column { top: 170px; left: 314px; width: 184px; font-size: 10px; }
  .about-column h2 { font-family: "Montserrat", sans-serif; font-size: 8.6px; letter-spacing: .2px; line-height: 15px; }
  .about-column p + h2 { margin-top: 15px; }

  .social-bar { position: absolute; top: 694px; left: 240px; width: 551px; border-top: 1px solid var(--rule); }
  .social-links { position: absolute; right: 14px; top: 6px; display: flex; gap: 18px; list-style: none; }
  .social-links a { color: #444; text-decoration: none; font-family: "Didact Gothic", sans-serif; font-size: 13px; line-height: 20px; }

  .portfolio-frame { position: absolute; top: 727px; left: 240px; width: 567px; height: 413px; border: 1px solid var(--frame); background: #fbfafc; }
  .portfolio-grid { position: absolute; top: 12px; left: 20px; width: 517px; height: 388px; }
  .tile { position: absolute; width: 129px; height: 129px; }
  .t1 { left: 0; top: 0; background: linear-gradient(160deg, #3a0d1a, #8a2030 55%, #d8d4cc); }
  .t2 { left: 129px; top: 0; background: linear-gradient(170deg, #1a120e, #4a3a22 50%, #8bb040 80%, #c44030); }
  .t3 { left: 258px; top: 0; background: linear-gradient(120deg, #f2efe8, #e8e2d6 50%, #c88a30 75%, #f4f0e8); }
  .t4 { left: 387px; top: 0; background: linear-gradient(180deg, #f0eeee, #d8d2d0 55%, #5a1c16); }
  .t5 { left: 0; top: 129px; background: linear-gradient(170deg, #2a1a14, #5a7040 45%, #d8cdc0 70%, #401c1c); }
  .t6 { left: 129px; top: 129px; height: 258px; background: linear-gradient(170deg, #1a1410, #4a7a30 40%, #e8ecdc 70%, #3c5a26); }
  .t7 { left: 258px; top: 129px; background: linear-gradient(150deg, #2c1612, #e8e0d0 45%, #8a4a2a); }
  .t8 { left: 387px; top: 129px; background: linear-gradient(180deg, #f6f4f2, #4a6ac8 30%, #bcb8b6 60%, #f0ecea); }
  .t9 { left: 0; top: 258px; background: linear-gradient(100deg, #8a2018, #c05a40 45%, #e8e0d8 65%, #5a1a10); }
  .t10 { left: 258px; top: 258px; width: 259px; background: linear-gradient(170deg, #f0e8e4, #c8a8a0 45%, #6a1a14 75%, #2a0808); }
  .portfolio-label { position: absolute; top: 129px; left: 106px; width: 311px; height: 46px; background: var(--label-bg);
    color: var(--white); font-family: "Didact Gothic", sans-serif; font-size: 42px; line-height: 44px; text-align: center; text-decoration: none; white-space: nowrap; }
  .portfolio-label .thin { color: #e6dde4; }

  .site-footer { position: absolute; top: 1163px; left: 260px; width: 522px; text-align: center; font-size: 8.4px; line-height: 9px; color: var(--ink-soft); }
</style>
</head>
<body>
  <nav class="site-nav">
    <a class="nav-home" href="#">home</a>
    <a class="nav-about" href="#">about maelis</a>
    <a class="nav-contact" href="#">contact her</a>
    <span class="lang-switch">chinese<span class="divider">|</span>english</span>
  </nav>

  <section class="about-panel">
    <div class="about-photo" role="img" aria-label="Portrait photograph of Maelis, warm orange to violet tones"></div>
    <span class="active-marker"></span>
    <p class="about-copy about-intro"><span class="drop-cap">L</span>orem ipsum dolor sit amet, consectetur adipiscing elit. Aliquam ultrices elit eu libero scelerisque lacinia. Mauris congue tellus rhoncus massa vestibulum rhoncus. In vestibulum nisi quis quam vestibulum viverra. Lorem ipsum dolor sit amet, consectetur adipiscing elit. Duis lorem nulla, interdum laoreet tristique at, scelerisque eu lacus. Aliquam a lectus quam, vel dignissim justo. Sed semper tempus rutrum. Nullam mattis iaculis ornare. Mauris tincidunt eleifend quam. Cras vehicula volutpat felis sed vestibulum. Proin luctus tortor id mi auctor vestibulum. Vivamus sed purus in ligula condimentum pretium ut a ipsum. Integer a gravida nisl. Vivamus commodo orci in sem vulputate viverra. Fusce pharetra ultrices pellentesque. In elementum ipsum gravida tellus blandit interdum.</p>
    <div class="about-copy about-column">
      <h2>ESTIBULUM NUNC QUAM</h2>
      <p>Vivamus egestas sagittis ligula at dapibus. Praesent dapibus, magna tincidunt cursus lacinia, urna tortor gravida leo, quis dapibus magna augue porta metus. Etiam consequat augue id orci faucibus fermentum. Ut pretium ullamcorper viverra. Vivamus quis nisl vel diam accumsan eleifend. Vestibulum nunc quam, mattis sed pellentesque non, euismod id eros. Donec sagittis odio eros, vitae pretium magna.</p>
      <h2>DOLOR SIT AMET</h2>
      <p>Donec ut nisi justo. Nulla vel velit leo. Etiam eget nisl nec mauris molestie cursus a nec nunc. Aliquam ultrices sapien at risus porttitor venenatis fermentum velit gravida. Nulla id quam justo. Nam lobortis adipiscing dui, sed tincidunt ante dapibus vitae.</p>
    </div>
  </section>

  <div class="social-bar">
    <ul class="social-links">
      <li><a href="#">chatnest</a></li>
      <li><a href="#">worklinq</a></li>
      <li><a href="#">vessa</a></li>
      <li><a href="#">xunmo</a></li>
    </ul>
  </div>

  <section class="portfolio-frame">
    <div class="portfolio-grid">
      <div class="tile t1" role="img" aria-label="Table set with red flowers and glassware"></div>
      <div class="tile t2" role="img" aria-label="Candles and a bowl of green apples"></div>
      <div class="tile t3" role="img" aria-label="Living room with a golden sculpture"></div>
      <div class="tile t4" role="img" aria-label="White lounge with pendant lamp and plant"></div>
      <div class="tile t5" role="img" aria-label="Dining table with floral centrepiece"></div>
      <div class="tile t6" role="img" aria-label="Close view of green and white flowers"></div>
      <div class="tile t7" role="img" aria-label="Candles on a cream table"></div>
      <div class="tile t8" role="img" aria-label="Blue hydrangeas in a silver vase"></div>
      <div class="tile t9" role="img" aria-label="Hallway with red artwork"></div>
      <div class="tile t10" role="img" aria-label="Living room with sofa and polished wooden floor"></div>
      <a class="portfolio-label" href="#"><span class="thin">view</span> portfolio</a>
    </div>
  </section>

  <footer class="site-footer">Aliquam sit amet ultricies lectus. Mauris at diam quis sem hendrerit dictum. Etiam consequat mauris at tellus viverra auctor. Phasellus sit amet neque ante. Suspendisse dignissim luctus sapien, nec ultrices metus rhoncus ut. Nulla non mauris arcu.</footer>
</body>
</html>
```